We need a fresh, new church business card!!

We need a church business card with basic info to hand out as invites. We are looking for something clean that communicates our basic information clearly.

We are open to square or rectangle card sizes.

General Public

Religious

The attached logo is the only one that I have available. We'd like to see options with with text of the logo lighter and on a dark background as well as options with white/light backgrounds.

Also, we'd like to see option with rounded corners.

• Address - 2718 Maple Row, Larkfield, LF 00142
• Website - brookvane.example
• Phone - 815-555-0163
• Service times -
• Sunday - 10am Sunday School
• - 11am Family Worship
• - 6pm Night of Prayer
• Wednesday - 7:30pm Adult Bible Study
• Classes for all ages

```html
<!DOCTYPE html>
<html lang="en">
<head>
<meta charset="utf-8">
<title>Brookvane Pentecostal Church – Business Card</title>
<link href="https://fonts.googleapis.com/css2?family=Open+Sans:wght@400;600;700&display=swap" rel="stylesheet">
<style>
  :root {
    --teal: #5b94a2;
    --white: #ffffff;
    --grey-swoosh: #7b7b7b;
    --logo-grey: #6e6e6e;
    --stage: #2c2c2c;
    --card-w: 800px;
    --card-h: 455px;
  }
  * { margin: 0; padding: 0; box-sizing: border-box; }
  html, body {
    width: 1000px; height: 1200px; overflow: hidden;
    background: var(--stage);
    font-family: "Open Sans", Arial, sans-serif;
  }
  .canvas { position: relative; width: 1000px; height: 1200px; }
  .card {
    position: absolute; left: 100px;
    width: var(--card-w); height: var(--card-h);
    overflow: hidden;
  }
  .card--front { top: 95px; background: var(--white); }
  .card--back { top: 650px; background: var(--teal); }

  .front-shapes { position: absolute; inset: 0; width: 100%; height: 100%; }

  .brand { position: absolute; left: 40px; top: 56px; display: flex; align-items: center; gap: 20px; }
  .brand__dot { width: 78px; height: 78px; border-radius: 50%; background: var(--teal); flex: none; }
  .brand__name { color: var(--logo-grey); font-weight: 600; line-height: 1; }
  .brand__name-main { display: block; font-size: 50px; letter-spacing: 1px; }
  .brand__name-sub { display: block; font-size: 17px; letter-spacing: 4.6px; margin-top: 6px; }

  .contact {
    position: absolute; left: 489px; top: 292px;
    color: var(--white); font-size: 21px; line-height: 29px;
  }
  .contact__row { display: flex; align-items: center; gap: 14px; margin-top: 4px; }
  .contact__row svg { width: 18px; height: 18px; flex: none; }
  .contact__address { margin-bottom: 4px; }

  .person-name {
    position: absolute; left: 30px; top: 378px;
    color: var(--white); font-size: 27px; font-weight: 700;
  }

  .back-mark {
    position: absolute; left: 82px; top: 102px;
    width: 204px; height: 204px; border-radius: 50%;
    background: var(--white);
    display: flex; align-items: center; justify-content: center;
    color: var(--teal); font-size: 30px; font-weight: 600;
  }
  .services { position: absolute; left: 345px; top: 118px; color: var(--white); }
  .services__title { font-size: 33px; font-weight: 600; margin-bottom: 12px; }
  .services__list { list-style: none; font-size: 22px; line-height: 30px; }
  .services__day { font-weight: 700; }
</style>
</head>
<body>
<main class="canvas">

  <section class="card card--front" aria-label="Card front">
    <svg class="front-shapes" viewBox="0 0 448 255" preserveAspectRatio="none" aria-hidden="true">
      <path d="M232,171 C335,140 405,80 428,0 L444,0 C420,85 345,148 232,171 Z" fill="#7b7b7b"/>
      <path d="M0,178 C210,176 390,110 448,0 L448,255 L0,255 Z" fill="#5b94a2"/>
    </svg>

    <div class="brand">
      <span class="brand__dot"></span>
      <span class="brand__name">
        <span class="brand__name-main">BROOKVANE</span>
        <span class="brand__name-sub">PENTECOSTAL CHURCH</span>
      </span>
    </div>

    <div class="contact">
      <p class="contact__address">2718 Maple Row, Larkfield<br>LF 00142</p>
      <p class="contact__row">
        <svg viewBox="0 0 24 24" aria-hidden="true"><path fill="#fff" d="M6.6 10.8a15.1 15.1 0 0 0 6.6 6.6l2.2-2.2a1 1 0 0 1 1-.25 11.4 11.4 0 0 0 3.6.57 1 1 0 0 1 1 1V20a1 1 0 0 1-1 1A17 17 0 0 1 3 4a1 1 0 0 1 1-1h3.5a1 1 0 0 1 1 1c0 1.25.2 2.45.57 3.57a1 1 0 0 1-.25 1Z"/></svg>
        <span>815-555-0163</span>
      </p>
      <p class="contact__row">
        <svg viewBox="0 0 24 24" aria-hidden="true" fill="none" stroke="#fff" stroke-width="2"><circle cx="12" cy="12" r="9.5"/><ellipse cx="12" cy="12" rx="4" ry="9.5"/><path d="M2.5 12h19M4 7h16M4 17h16"/></svg>
        <span>brookvane.example</span>
      </p>
    </div>

    <p class="person-name">Person Name</p>
  </section>

  <section class="card card--back" aria-label="Card back">
    <div class="back-mark">Brookvane</div>
    <div class="services">
      <h2 class="services__title">Service times</h2>
      <ul class="services__list">
        <li><span class="services__day">Sunday</span> - 10am Sunday School</li>
        <li>11am Family Worship</li>
        <li>6pm Night of Prayer</li>
        <li><span class="services__day">Wednesday</span> - 7:30pm Adult Bible Study</li>
        <li>Classes for all ages</li>
      </ul>
    </div>
  </section>

</main>
</body>
</html>
```